Alloy wheel repair business needs a website

Install logo previously purchased from pixelbazaar, toolbar with dropdowns. services, gallery, clients , contact ect
Maybe mission statment

Target Market(s)

vehicle owners, auto dealers,insurance companies,

Industry/Entity Type

Alloy Wheel Repair

Coding

Coded - Design and coding required

Number of Pages Required

4 page

Font styles to use
Sans Serif

Colors
0054AA
0677BA
7BADD7
CADEEF
E8F1F8

```html
<!DOCTYPE html>
<html lang="en">
<head>
<meta charset="utf-8">
<title>Rimforge Studio — Alloy Wheel Repair</title>
<link href="https://fonts.googleapis.com/css2?family=Audiowide&family=Lato:wght@400;700;900&display=swap" rel="stylesheet">
<style>
:root{
  --blue:#3d87c7;
  --blue-deep:#0054AA;
  --navy:#1d2c49;
  --ink:#1b1b1b;
  --text:#454545;
  --dark:#1c1c1c;
  --white:#ffffff;
  --star:#f5a01a;
}
*{margin:0;padding:0;box-sizing:border-box}
html,body{width:1200px;height:3379px;overflow:hidden}
body{position:relative;background:var(--white);font-family:'Lato',sans-serif;color:var(--text)}
.abs{position:absolute}
.display{font-family:'Audiowide',sans-serif;letter-spacing:2px}

/* header */
.site-header{left:0;top:0;width:1200px;height:93px;background:var(--white)}
.brand{display:flex;align-items:center;gap:10px;font-family:'Lato',sans-serif;font-weight:900;font-size:27px;letter-spacing:1px;text-transform:uppercase}
.brand-dot{width:22px;height:22px;border-radius:50%;background:var(--blue)}
.site-header .brand{left:118px;top:28px;color:var(--navy)}
.main-nav{left:0;top:34px;width:1200px;font-size:15px;color:#555}
.main-nav a{position:absolute;color:inherit;text-decoration:none}
.main-nav a.active{color:var(--ink);font-weight:700}
.btn{display:flex;align-items:center;justify-content:center;background:var(--blue);color:var(--white);font-size:15px;text-decoration:none}
.btn-header{left:961px;top:24px;width:127px;height:40px}

/* hero */
.hero{left:0;top:93px;width:1200px;height:530px}
.hero-copy{left:520px;top:114px;width:600px;text-align:center;color:var(--white)}
.hero-copy .pre{font-size:29px;line-height:1}
.hero-copy .big{font-size:60px;line-height:72px;margin-top:14px}

/* section titles */
.section-title{left:0;width:1200px;text-align:center;color:var(--blue);font-size:40px}

/* services */
.service-card{width:296px;height:325px;top:748px;background:var(--white);box-shadow:0 4px 18px rgba(0,0,0,.07);text-align:center;border-radius:4px}
.service-card svg{margin-top:32px}
.service-card h3{margin-top:18px;font-size:17px;font-weight:700;color:var(--ink)}
.service-card p{margin:22px auto 0;width:250px;font-size:15px;line-height:26px}

/* about */
.about{left:0;top:1110px;width:1200px;height:615px}
.about-copy{left:113px;top:1250px;width:560px;color:var(--white)}
.about-copy h2{font-size:40px;color:var(--white)}
.about-copy p{font-size:15px;line-height:28px;margin-top:20px;text-align:justify}
.about-copy h4{font-size:15px;font-weight:700;margin-top:10px}
.about-copy h4 + p{margin-top:4px}
.btn-about{left:113px;top:1571px;width:127px;height:41px}

/* gallery */
.gallery-tile{display:block}

/* testimonials */
.testimonial{width:308px;height:253px;top:2615px;background:var(--white);box-shadow:0 4px 18px rgba(0,0,0,.07);padding:30px 20px 0 20px}
.stars{display:flex;gap:5px}
.testimonial p{margin-top:22px;font-size:15px;line-height:27.5px}
.reviewer{top:2894px;display:flex;align-items:center;gap:16px}
.avatar{width:56px;height:56px;border-radius:50%;background:linear-gradient(160deg,#d8c7b4,#8a6e58);border:2px solid #ddd}
.reviewer b{display:block;font-size:16px;color:var(--ink);font-weight:700}
.reviewer span{display:block;font-size:15px;margin-top:4px}

/* footer */
.site-footer{left:0;top:3000px;width:1200px;height:379px}
.site-footer .brand{left:112px;top:3134px;color:var(--white)}
.footer-about{left:112px;top:3200px;width:330px;color:var(--white);font-size:15px;line-height:28px}
.footer-col{top:3110px;color:var(--white)}
.footer-col h5{font-size:16px;font-weight:700;margin-bottom:14px}
.footer-col li{list-style:none;font-size:15px;line-height:30px}
.copyright{left:0;top:3338px;width:1200px;text-align:center;color:var(--white);font-size:15px}
</style>
</head>
<body>

<header class="site-header abs">
  <div class="brand abs"><span class="brand-dot"></span>Rimforge Studio</div>
  <nav class="main-nav abs">
    <a class="active" style="left:568px">Home</a>
    <a style="left:635px">Services</a>
    <a style="left:716px">Gallery</a>
    <a style="left:791px">Clients</a>
    <a style="left:863px">Contact</a>
  </nav>
  <a class="btn btn-header abs">Get Started</a>
</header>

<section class="hero abs">
  <svg width="1200" height="530" viewBox="0 0 1200 530" role="img" aria-label="Photo of a polished multi-spoke alloy wheel resting on a tyre in a dark workshop">
    <defs>
      <radialGradient id="heroPhoto" cx="0.25" cy="0.45" r="0.7">
        <stop offset="0" stop-color="#8e8e8e"/>
        <stop offset="0.35" stop-color="#3c3c3c"/>
        <stop offset="1" stop-color="#121212"/>
      </radialGradient>
    </defs>
    <polygon points="0,0 1200,0 1200,425 0,507" fill="url(#heroPhoto)"/>
    <polygon points="112,500 1200,425 1200,445 112,518" fill="var(--blue)"/>
  </svg>
</section>
<div class="hero-copy display abs">
  <div class="pre">WELCOME TO</div>
  <div class="big">RIMFORGE<br>STUDIO</div>
</div>

<h2 class="section-title display abs" style="top:656px">OUR SERVICES</h2>

<article class="service-card abs" style="left:114px">
  <svg width="90" height="90" viewBox="0 0 90 90" fill="none" stroke="#2f4a6e" stroke-width="3">
    <circle cx="45" cy="45" r="42"/><circle cx="45" cy="45" r="33"/><circle cx="45" cy="45" r="8"/>
    <path d="M45 37V12M52 42L76 34M50 52L64 72M40 52L26 72M38 42L14 34"/>
  </svg>
  <h3>LOREM IPSUM</h3>
  <p>Sed ut perspiciati unde omnis iste natus error sit voluptm accusantium doloremque laudantium, totam rem. rror sit voluptm accusanti</p>
</article>
<article class="service-card abs" style="left:452px">
  <svg width="90" height="90" viewBox="0 0 90 90" fill="none" stroke="#2f4a6e" stroke-width="3">
    <circle cx="45" cy="45" r="42" stroke-dasharray="6 4"/><circle cx="45" cy="45" r="30"/><circle cx="45" cy="45" r="8"/>
    <path d="M55 38L80 22M55 52L80 68" stroke="var(--blue)"/>
  </svg>
  <h3>LOREM IPSUM</h3>
  <p>Sed ut perspiciati unde omnis iste natus error sit voluptm accusantium doloremque laudantium, totam rem. rror sit voluptm accusanti</p>
</article>
<article class="service-card abs" style="left:792px">
  <svg width="110" height="90" viewBox="0 0 110 90" fill="none" stroke="#2f4a6e" stroke-width="3">
    <rect x="38" y="4" width="68" height="26" rx="4"/><rect x="38" y="32" width="68" height="26" rx="4"/><rect x="38" y="60" width="68" height="26" rx="4"/>
    <circle cx="38" cy="52" r="34" fill="#fff" stroke="var(--blue)"/><circle cx="38" cy="52" r="22"/><circle cx="38" cy="52" r="6"/>
  </svg>
  <h3>LOREM IPSUM</h3>
  <p>Sed ut perspiciati unde omnis iste natus error sit voluptm accusantium doloremque laudantium, totam rem. rror sit voluptm accusanti</p>
</article>

<section class="about abs">
  <svg width="1200" height="615" viewBox="0 0 1200 615">
    <defs>
      <linearGradient id="aboutPhoto" x1="0" x2="1" y1="0" y2="0">
        <stop offset="0" stop-color="#262626"/>
        <stop offset="0.45" stop-color="#3a332c"/>
        <stop offset="0.75" stop-color="#7d7d7d"/>
        <stop offset="1" stop-color="#3b3b3b"/>
      </linearGradient>
    </defs>
    <polygon points="0,81 1200,6 1200,520 0,595" fill="url(#aboutPhoto)" role="img" aria-label="Close-up photo of a chrome alloy wheel with an orange brake caliper"/>
    <polygon points="77,590 1200,520 1200,540 77,612" fill="var(--blue)"/>
  </svg>
</section>
<div class="about-copy abs">
  <h2 class="display">ABOUT US</h2>
  <p>Sed ut perspiciatis unde omnis iste natus error sit voluptatem accusantium doloremque laudantium, totam rem aperiam, eaque ipsa quae ab illo inve ntore veritatis et quasi architecto beatae vitae dicta sunt explicabo.</p>
  <h4>OUR MISSION</h4>
  <p>Nemo enim ipsam voluptatem quia voluptas sit aspernatur aut odit aut fugit, sed quia consequuntur magni dolores eos qui ratione voluptatem sequi nesciunt. Neque porro quisquam est, qui dolorem ipsum quia dolor sit amet, consectetur</p>
</div>
<a class="btn btn-about abs">Learn More</a>

<h2 class="section-title display abs" style="top:1771px">GALLERY</h2>
<div class="gallery-tile abs" style="left:112px;top:1894px;width:312px;height:254px;background:linear-gradient(135deg,#c96a2a,#2b1f1c 55%,#5a5d63)" role="img" aria-label="Photo of a black and silver alloy wheel with a red brake caliper"></div>
<div class="gallery-tile abs" style="left:443px;top:1894px;width:312px;height:254px;background:linear-gradient(135deg,#2b3c73,#9aa0a8 50%,#eef0f2)" role="img" aria-label="Photo of a technician fitting a wheel with an impact wrench"></div>
<div class="gallery-tile abs" style="left:776px;top:1894px;width:312px;height:254px;background:linear-gradient(135deg,#5b5b5b,#2a2624 45%,#b8701c 60%,#262626)" role="img" aria-label="Photo of a dark alloy wheel with an orange brake caliper"></div>
<div class="gallery-tile abs" style="left:112px;top:2172px;width:643px;height:254px;background:linear-gradient(90deg,#d9a433,#c24a26 35%,#2a2a2a 60%,#b35a22 80%,#1e1e1e)" role="img" aria-label="Photo of a yellow sports car beside a black and orange alloy wheel"></div>
<div class="gallery-tile abs" style="left:776px;top:2172px;width:312px;height:254px;background:radial-gradient(circle at 55% 55%,#9a9a9a,#2e2e2e 60%,#111)" role="img" aria-label="Black and white photo of alloy wheels displayed on a wall"></div>

<h2 class="section-title display abs" style="top:2520px">CLIENT TESTIMONIALS</h2>

<article class="testimonial abs" style="left:114px">
  <div class="stars">
    <svg width="98" height="16" viewBox="0 0 98 16" fill="var(--star)"><g id="s"><polygon points="8,0 10,6 16,6 11,10 13,16 8,12 3,16 5,10 0,6 6,6"/></g><use href="#s" x="20"/><use href="#s" x="40"/><use href="#s" x="60"/><use href="#s" x="80"/></svg>
  </div>
  <p>Sed ut perspiciatis unde omnis iste natus error sit voluptatem accusantium dolor emque laudantium, totam rem aperiam, eaque ipsa quae ab illo inventore verita tis et quasi architecto beatae vitae dicta sunt explicabo.</p>
</article>
<article class="testimonial abs" style="left:447px">
  <div class="stars"><svg width="98" height="16" viewBox="0 0 98 16" fill="var(--star)"><use href="#s"/><use href="#s" x="20"/><use href="#s" x="40"/><use href="#s" x="60"/><use href="#s" x="80"/></svg></div>
  <p>Sed ut perspiciatis unde omnis iste natus error sit voluptatem accusantium dolor emque laudantium, totam rem aperiam, eaque ipsa quae ab illo inventore verita tis et quasi architecto beatae vitae dicta sunt explicabo.</p>
</article>
<article class="testimonial abs" style="left:780px">
  <div class="stars"><svg width="98" height="16" viewBox="0 0 98 16" fill="var(--star)"><use href="#s"/><use href="#s" x="20"/><use href="#s" x="40"/><use href="#s" x="60"/><use href="#s" x="80"/></svg></div>
  <p>Sed ut perspiciatis unde omnis iste natus error sit voluptatem accusantium dolor emque laudantium, totam rem aperiam, eaque ipsa quae ab illo inventore verita tis et quasi architecto beatae vitae dicta sunt explicabo.</p>
</article>

<div class="reviewer abs" style="left:112px"><div class="avatar" role="img" aria-label="Client portrait"></div><div><b>JAMES</b><span>June 01,2022</span></div></div>
<div class="reviewer abs" style="left:446px"><div class="avatar" role="img" aria-label="Client portrait"></div><div><b>JAMES</b><span>June 01,2022</span></div></div>
<div class="reviewer abs" style="left:779px"><div class="avatar" role="img" aria-label="Client portrait"></div><div><b>JAMES</b><span>June 01,2022</span></div></div>

<footer class="site-footer abs">
  <svg width="1200" height="379" viewBox="0 0 1200 379">
    <polygon points="0,86 1200,8 1200,379 0,379" fill="var(--dark)"/>
    <polygon points="0,69 1053,3 1053,17 0,86" fill="var(--blue)"/>
  </svg>
</footer>
<div class="brand abs" style="left:112px;top:3134px;color:var(--white)"><span class="brand-dot"></span>Rimforge Studio</div>
<p class="footer-about abs">Sed ut perspiciatis unde omnis iste natus error sit voluptatem accusantium doloremque lau dantium, totam rem aperiam, eaque ipsa.</p>
<div class="footer-col abs" style="left:547px">
  <h5>Quick links</h5>
  <ul><li>Home</li><li>About</li><li>Services</li><li>Clients</li></ul>
</div>
<div class="footer-col abs" style="left:787px">
  <h5>Support links</h5>
  <ul style="margin-top:3px"><li>Warranty</li><li>Returns</li><li>Contact</li></ul>
</div>
<div class="footer-col abs" style="left:1013px">
  <h5>Follow Us</h5>
  <ul style="margin-top:3px"><li>Socialhub</li><li>Snapgram</li><li>Chirper</li></ul>
</div>
<p class="copyright abs">©Copyrights 2023 Rimforge Studio. All Rights Reserved.</p>

</body>
</html>
```